Brovanta Cargo Flower trade show brochure

We are an international freight forwarding company from South America specialising in perishable handling both through air freight and sea freight. We need a brochure to hand out to customers in the flower fair trade shows in which we participate - China, Holland, Russia, USA. We need something clean yet striking and modern emphasising our brand and with great emphasis on our strengths in the perishable/flower forwarding realm. Our company is a merger of 4 of the largest forwarders in Ecuador into one company called Brovanta Cargo Group. We would like emphasis on the new brand, however we do require that each individual logo of the 4 companies is portrayed in some way in the brochure. We are also registered with a global freight forwarding association known as PFN which also must be mentioned. We would like a defined concept for perishable handling, something along the lines of (but not limited to) - first class travel - dont your flowers deserve the same ? Attached a JPEG file with our new website proposed design so that you have an idea of our tastes. Also attached is some basic text which can be used to put together the brochure. We would like some emphasis also on some fast data facts such as - 1. We ship to over 80 countries worldwide 2. we forward over 5000 tons of flowers per month 3. we track and trace over 150 shipments per day etc etc. Please also include our website adress - www.brovantacargo, and something along the lines of - Follow us on (logo Netlyst), (logo Chatterbox), logo (quipper) and our contact email address - info@brovantacargo.example

Target Market(s)

Flower importers worldwide

Industry/Entity Type

Freight Forwarding

Font styles to use
Sans Serif

Colors
9bcb3b
acd036
9d9d9d
757575

Requirements
Must have
• Photos of freight forwarding concepts, cut flowers

```html
<!DOCTYPE html>
<html lang="en">
<head>
<meta charset="utf-8">
<title>Brovanta Cargo Group – Trifold Brochure</title>
<link href="https://fonts.googleapis.com/css2?family=Open+Sans:wght@400;600;700&display=swap" rel="stylesheet">
<style>
  :root {
    --green: #9bcb3b;
    --green-light: #acd036;
    --grey: #9d9d9d;
    --grey-dark: #757575;
    --ink: #2e2e2e;
    --paper: #ffffff;
    --stage: #4a4a4a;
  }
  * { box-sizing: border-box; margin: 0; padding: 0; }
  html, body {
    width: 937px; height: 1200px; overflow: hidden;
    background: var(--stage);
    font-family: "Open Sans", Arial, sans-serif;
    color: var(--ink);
  }
  .brochure {
    position: absolute; left: 28px; top: 260px;
    width: 880px; height: 680px;
    display: grid; grid-template-columns: repeat(3, 1fr);
    background: var(--paper);
    box-shadow: 0 20px 40px rgba(0,0,0,.45);
  }
  .panel { position: relative; overflow: hidden; }
  .panel--middle { background: linear-gradient(90deg, #f1f1f1 0%, #ffffff 18%, #ffffff 82%, #f3f3f3 100%); }
  .panel--right { background: linear-gradient(90deg, #f6f6f6 0%, #ffffff 15%); }

  /* Cover panel */
  .cover-band {
    height: 170px; background: var(--green);
    display: flex; align-items: flex-end; padding: 0 0 86px 70px;
  }
  .cover-band__url { color: var(--paper); font-size: 11px; }
  .brand {
    display: flex; align-items: center; justify-content: center; gap: 8px;
    margin-top: 120px;
  }
  .brand__mark { width: 14px; height: 14px; background: var(--green); }
  .brand__name { font-size: 22px; font-weight: 700; color: #3a3a3a; letter-spacing: -.3px; }
  .intro {
    position: absolute; left: 26px; right: 26px; bottom: 46px;
    font-size: 10.5px; line-height: 1.42; text-align: justify;
  }

  /* Photo across middle and right panels */
  .photo {
    position: absolute; left: 293px; top: 0; width: 587px; height: 230px;
    background:
      radial-gradient(circle at 30% 60%, rgba(230,190,40,.85) 0 12%, transparent 26%),
      radial-gradient(circle at 70% 35%, rgba(200,40,70,.7) 0 10%, transparent 24%),
      radial-gradient(circle at 85% 75%, rgba(240,210,60,.8) 0 10%, transparent 22%),
      radial-gradient(circle at 50% 20%, rgba(80,70,160,.5) 0 8%, transparent 20%),
      linear-gradient(160deg, #d9c39a 0%, #4f7a2e 40%, #3e6a26 65%, #cdb58a 100%);
  }

  .content { padding: 252px 26px 0; font-size: 10.5px; line-height: 1.42; text-align: justify; }
  .content p + p { margin-top: 14px; }
  .label { color: var(--green); font-weight: 700; text-transform: uppercase; }
  .heading { color: var(--green); font-weight: 700; font-size: 11px; text-transform: uppercase; margin-bottom: 2px; }
  .services-heading { color: var(--green-light); font-weight: 700; font-size: 11px; text-transform: uppercase; margin: 44px 0 20px 30px; }
  .services { list-style: none; padding-left: 30px; font-size: 6.6px; line-height: 1.3; color: var(--grey-dark); text-align: left; }
  .services li + li { margin-top: 6px; }
  .tagline {
    position: absolute; right: 20px; bottom: 40px;
    color: var(--green); font-size: 10px;
  }
  .base-strip { position: absolute; left: 0; right: 0; bottom: 0; height: 12px; background: var(--green); }
  .panel--right .base-strip { height: 26px; }
</style>
</head>
<body>
  <main class="brochure">
    <section class="panel panel--cover">
      <div class="cover-band"><span class="cover-band__url">www.brovantacargo.com</span></div>
      <div class="brand"><span class="brand__mark"></span><span class="brand__name">Brovanta Cargo</span></div>
      <p class="intro">Brovanta Cargo Group is an International Freight Forwarding company operating from Quito, Guayaquil, Bogota, Medellin and Miami with more than 75 years of combined expertise in perishable handling. We are the leading perishable handler out of Ecuador, focused on providing personalized service in a reliable and timely manner.</p>
      <div class="base-strip"></div>
    </section>

    <section class="panel panel--middle">
      <div class="content">
        <p><span class="label">Network:</span> Apart from our own offices and warehouses in Ecuador, Colombia and the USA, Brovanta Cargo has developed a strategic network that fulfills your logistics and freight forwarding needs worldwide. Our network includes more than 5000 registered PFN partners globally.</p>
        <p><span class="label">Experience:</span> Our experienced staff understand our customers' needs and focus on providing a comprehensive logistic experience with unparalleled service. We understand that accurate and timely information is just as important as the shipment itself.</p>
        <p><span class="label">Infrastructure:</span> With 4600m2 of refrigerated and dry storage, 20 dock-shelters and pallet build up for our clients inside the airline's warehouse, you can trust that your product is in safe hands with this unique service in Ecuador.</p>
        <p><span class="label">Innovation:</span> Brovanta Cargo is dedicated to continual improvement and an innovative approach to freight forwarding. We are currently in the process of upgrading our tailor made and industry specific software in order to provide faster, more accurate and more detailed information to our customers.</p>
      </div>
      <div class="base-strip"></div>
    </section>

    <section class="panel panel--right">
      <div class="content">
        <h2 class="heading">Freight Forwarding</h2>
        <p>As an IATA agent for all major airlines, we can offer our customers reliable and varied options for their perishable forwarding requirements. Our expert staff work tirelessly to ensure that your temperature sensitive cargo arrives to its destination using optimal routings and maximum cost-efficiency.</p>
      </div>
      <h2 class="services-heading">Value-Added Services</h2>
      <ul class="services">
        <li>Leveraged purchasing power with all major carriers</li>
        <li>Tracking and tracing follow-up on all shipments</li>
        <li>Customized labelling and handling</li>
        <li>Gross vs chargeable reports by supplier</li>
        <li>Temperature and humidity control monitoring</li>
        <li>Customized shipment reporting</li>
        <li>Temperature control reports per supplier</li>
        <li>State of the art CCTV security systems ensuring your products integrity whilst in our possession</li>
        <li>ISO 9001 Quality certified processes</li>
        <li>PFN member since January 2015 - 5000 PFN partners all over the world</li>
        <li>Ability to offer full ULDs</li>
      </ul>
      <p class="tagline">Our success depends on the success of our customers</p>
      <div class="base-strip"></div>
    </section>

    <div class="photo" role="img" aria-label="Photo of wooden crates filled with colourful potted flowers in yellow, red and purple"></div>
  </main>
</body>
</html>
```